Calloway Aeronautics website

We are an aviation company based in Miramar, FL but with worldwide coverage. We are involved in commercial aircraft (mostly freighters) trading, sale & leasing. Specifically, we specialized in freighters of the Vantrex family (V310, V320, V330, V340, V350). We also assist with financing, sale/leaseback. Handle special aviation projects and provide consultancy services. Currently engaged in a Vantrex 350 passenger to Freighter conversion (P2F).

Website Preliminary Initial Content/Sections as follows:

About Us
Founded in 2011, Calloway Aeronautics' management has many years of experience in Aviation, a strong background in scheduled airlines with emphasis in all cargo operations, freight forwarding supply chain and freight logistics, as well as ACMI and CMI operations.

Calloway’s focuses in facilitating wet and dry lease operations, charter and ACMI programs consultancy, aircraft sales, leasing and procurement, aviation consultancy and aircraft management.

Calloway team is a hands-on reliable alternative that works toward achieving your aircraft and aviation objectives by meeting your requirements and timeframe throughout professional and personalized service.

Teodoro Lasalle has over three decades of experience in the aviation field including aircraft maintenance, airline management, supply chain and logistics management. Teodoro is a true entrepreneur with proven experience and expertise on the multiple facets of the commercial aviation industry throughout the creation and development of a cluster of aviation entities. Teodoro is the founder and former sole member/chairman of 64 Jet, a Vantrex 340 All-Cargo U.S. Certificated Air Carrier created from scratch in 2014 which nowadays conforms a superb growing airline platform with an immaculate compliance operational record.

Services

Aircraft Finance, Trading, Procurement and Leasing
Calloway buys, sells, leases and facilitates aircraft trading while specializes in structured aircraft investment projects. Calloway has deep industry relationships and years of expertise, allowing to successfully execute lease transactions. We assist airlines, financial institutions and leasing companies when selling or purchasing aircraft.

Aircraft Available for Sale/Lease

Sale/Leaseback
Sale-leaseback is a method of financing. If your company needs liquidity, your aircraft or engine can serve as collateral for a loan throughout a sale-leaseback transaction. Sale-leaseback can free the equity tied up in aircraft or asset. Even if there is no pressing need for funds, a sale-leaseback allows you to use the equity tied up in your aircraft in a more productive fashion. Leaseback arrangements are usually employed because they confer financing, accounting or taxation benefits.

Passenger to Freighter Conversion (P2F)
Pandemic has seen the resurgence of operators packing freight into the main cabins of passenger aircraft. Carriers have been allowed to transport cargo in the cabin by removing passenger seats completely. NCA/ORSA have established exemptions that allow operators to fly in “Preighter” configuration for a limited time. Calloway is closely working with a U.S. group that is developing a Class E Supplemental Type Certificate (STC) for applicability on V350 aircraft which will include a cargo door for containerized freight. Final approvals are expected during first quarter of 2022.
Wet lease
Throughout our deep relationships within the industry, Calloway facilitates short or long-term wet leases to airlines and qualified parties around the globe, whereby we provide the Aircraft, Crews, Maintenance and Insurance (ACMI) worldwide services at competitive rates. We also specialize in AM leases where the aircraft is registered onto Lessee´s AOC with all maintenance services included in the rates, covering all maintenance risks, or CM or CMI where the client provides the aircraft.

Dry Lease
We offer aircraft from our own portfolio on dry lease or could engage in procuring the aircraft of your choice.

Asset & Aircraft Management
We provide aircraft owners Aircraft Management services, where we manage the technical side of the aircraft or the asset. Calloway also provides Harwick Dynamo engines trading, repair and full management services. We also buy Vantrex/Skylane surplus inventory.

Worldwide Charters
We facilitate the arrangement of full charters to airlines and logistics companies. Certain territory restrictions may apply.

Aviation Consultancy
We provide airline consultancy services for new or special projects. Calloway also specializes on All Cargo International route analysis, implementation and development. Our team provides professional guidance in obtaining worldwide both scheduled and charter authority.

Target Market(s)

Our target market are the airlines, logistics companies and commercial aviation related entities

Industry/Entity Type

Commercial Aviation

Coding

Number of Pages Required

3 page

Requirements
Must have
• Illustrations of wide body freighters such V350, V340, V320

```html
<!DOCTYPE html>
<html lang="en">
<head>
<meta charset="utf-8">
<title>Calloway Aeronautics – Homepage Layouts</title>
<link rel="stylesheet" href="https://fonts.googleapis.com/css2?family=Cinzel:wght@400;500&family=Poppins:wght@400;500;600&display=swap">
<style>
:root{
  --board:#bccad0;
  --navy:#0b1550;
  --navy-mid:#14246a;
  --ink:#0d1a55;
  --body:#5b6170;
  --soft:#c9d0e2;
  --pill:#98a4b5;
  --pill-dark:#7d8a9d;
  --card-grey:#e5e8ed;
  --white:#ffffff;
  --serif:'Cinzel', serif;
  --sans:'Poppins', sans-serif;
}
*{box-sizing:border-box;margin:0;padding:0}
html,body{width:1200px;height:2242px;overflow:hidden;background:var(--board)}
.board{position:relative;width:1200px;height:2242px;background:var(--board)}
.page{position:absolute;width:468px;background:var(--white);overflow:hidden;font-family:var(--sans);color:var(--body)}
.page--full{left:92px;top:67px;height:2107px}
.page--alt{left:623px;top:67px;height:2030px}
.band{position:absolute;left:0;top:0;width:468px}

/* navigation */
.nav-link{position:absolute;top:22px;font-family:var(--serif);font-size:8.6px;letter-spacing:.4px;color:var(--white)}
.nav-link--active::after{content:"";position:absolute;left:0;right:0;top:14px;height:2px;background:var(--white)}
.brand{position:absolute;top:17px;left:153px;width:140px;text-align:center;font-family:var(--serif);color:var(--white);font-weight:400}
.brand-name{display:block;font-size:11.5px;line-height:13px;letter-spacing:.8px}
.brand-sub{display:block;font-size:6px;line-height:9px;letter-spacing:3.2px}

.hero-title{position:absolute;left:43px;top:95px;font-family:var(--serif);font-weight:400;font-size:21px;line-height:35px;letter-spacing:1.2px;color:var(--white)}

.pill{position:absolute;display:flex;align-items:center;justify-content:center;border-radius:12px;font-family:var(--serif);color:var(--white);background:linear-gradient(90deg,var(--pill-dark),var(--pill));letter-spacing:.3px}
.pill--navy{background:var(--navy)}

.section-title{position:absolute;font-family:var(--serif);font-weight:400;font-size:18px;line-height:22px;letter-spacing:.8px;color:var(--ink)}
.section-title--center{left:0;width:468px;text-align:center}
.section-title--light{color:var(--white)}
.lead{position:absolute;font-size:6.4px;line-height:10.6px;color:#4b5060}

.divider-dot{position:absolute;width:9px;height:9px;margin-left:-4.5px;margin-top:-4.5px;border-radius:50%;background:radial-gradient(circle,#e8ecf4,#9aa6bd)}
.divider-line{position:absolute;left:233.5px;width:1px;background:var(--navy)}

/* service cards */
.card{position:absolute;width:117px;background:var(--white);border-radius:10px 24px 4px 4px;box-shadow:0 3px 8px rgba(20,30,70,.10);overflow:hidden;text-align:center}
.card-photo{width:117px;height:104px}
.card-title{margin-top:14px;padding:0 8px;font-size:8.6px;line-height:10.5px;font-weight:600;color:#2a2f3e}
.card-text{margin-top:4px;padding:0 12px;font-size:5.6px;line-height:7.2px;color:#6a6f7c}
.card-btn{display:inline-flex;margin-top:8px;width:52px;height:14px;border-radius:7px;align-items:center;justify-content:center;background:linear-gradient(90deg,var(--pill-dark),var(--pill));color:var(--white);font-size:4.8px;font-weight:600;letter-spacing:.3px}

/* about */
.about-photo{position:absolute;width:148px;height:148px;border-radius:50%;border:3px solid var(--white);box-shadow:0 0 0 4px #13206a,0 0 0 5.5px var(--white);background:linear-gradient(160deg,#7fb7d8 0%,#e3b3b6 38%,#6b7d96 62%,#3b4258 100%)}
.about-text{position:absolute;width:186px;font-size:6.2px;line-height:10.4px;color:var(--soft)}
.about-text p+p{margin-top:10px}

/* features */
.feat-icon{position:absolute;width:38px;height:38px;border-radius:50%;background:var(--navy);display:flex;align-items:center;justify-content:center}
.feat-copy{position:absolute;width:82px}
.feat-title{font-size:7.6px;line-height:9px;font-weight:500;color:#1d2233}
.feat-text{margin-top:2px;font-size:5.2px;line-height:6.4px;color:#7a7f8a}
.bracket{position:absolute;width:14px;height:14px;border-color:var(--navy);border-style:solid;border-width:0}
.ornament{position:absolute;left:204px;top:1086px;width:60px;height:60px;border-radius:50%;background:radial-gradient(circle,#7b8ea8 0%,rgba(123,142,168,.35) 45%,rgba(255,255,255,0) 72%)}

/* service icons */
.svc{position:absolute;width:90px;text-align:center}
.svc-icon{width:52px;height:52px;margin:0 auto;border-radius:50%;background:var(--navy);display:flex;align-items:center;justify-content:center}
.svc-label{margin-top:6px;font-size:8px;font-weight:600;color:var(--ink)}

/* contact */
.contact-sub{position:absolute;left:0;width:468px;text-align:center;font-size:8.4px;line-height:11px;color:#d3d9e8}
.field-label{position:absolute;font-size:5.4px;color:#c9cfe0}
.field-line{position:absolute;height:1px;background:#8f9bbb}

/* news */
.news-main{position:absolute;width:198px;height:213px;border-radius:6px 22px 6px 6px;overflow:hidden;background:var(--navy)}
.news-main-photo{position:absolute;inset:0;background:linear-gradient(180deg,#9fb4cf 0%,#c5ced9 30%,#6f83a6 52%,#1c2c6a 72%,var(--navy) 100%)}
.news-main-title{position:absolute;left:36px;top:124px;font-family:var(--serif);font-weight:400;font-size:11px;line-height:14px;color:var(--white);letter-spacing:.3px}
.news-main-text{position:absolute;left:36px;top:170px;width:140px;font-size:6.4px;line-height:8.4px;font-weight:600;color:var(--white)}
.news-item{position:absolute;width:166px;height:103px;border-radius:4px 16px 4px 4px;background:var(--card-grey)}
.news-thumb{position:absolute;left:9px;top:9px;width:65px;height:85px;border-radius:50%}
.news-date{position:absolute;left:85px;top:18px;font-size:4.8px;font-weight:600;color:#1d2233}
.news-title{position:absolute;left:85px;top:30px;width:72px;font-family:var(--serif);font-weight:400;font-size:6px;line-height:7.4px;color:#1d2233}
.news-text{position:absolute;left:85px;top:56px;width:70px;font-size:4.8px;line-height:6px;color:#5d6270}

/* footer */
.foot-brand{position:absolute;left:0;width:468px;text-align:center;font-family:var(--serif);font-weight:400;color:var(--white)}
.foot-item{position:absolute;display:flex;align-items:center;gap:6px;font-size:6.8px;line-height:9px;color:var(--white);white-space:nowrap}
.foot-icon{width:17px;height:17px;border-radius:50%;background:#8793a6;display:flex;align-items:center;justify-content:center;flex:none}
.copyright{position:absolute;left:0;width:468px;text-align:center;font-size:5.8px;letter-spacing:1px;font-weight:500;color:var(--white)}
</style>
</head>
<body>
<main class="board">

<!-- ============ Full layout ============ -->
<section class="page page--full">
  <svg class="band" width="468" height="2107" viewBox="0 0 468 2107" role="img" aria-label="Airliner flying head-on through a dusk sky over a city">
    <defs>
      <linearGradient id="heroSkyA" x1="0" y1="0" x2="0" y2="1">
        <stop offset="0" stop-color="#1f2d6c"/><stop offset=".55" stop-color="#4b5391"/><stop offset="1" stop-color="#8e809f"/>
      </linearGradient>
    </defs>
    <polygon points="0,0 468,0 468,233 234,264 0,233" fill="url(#heroSkyA)"/>
  </svg>
  <svg class="band" width="468" height="2107" viewBox="0 0 468 2107" role="img" aria-label="Deep blue cloudscape behind the about section">
    <defs>
      <radialGradient id="aboutSkyA" cx=".55" cy=".45" r=".8">
        <stop offset="0" stop-color="#1e3a8c"/><stop offset="1" stop-color="#0a1552"/>
      </radialGradient>
    </defs>
    <polygon points="0,673 234,640 468,673 468,886 234,916 0,886" fill="url(#aboutSkyA)"/>
  </svg>
  <svg class="band" width="468" height="2107" viewBox="0 0 468 2107" role="img" aria-label="Wide-body freighter taking off from a runway, fading into navy">
    <defs>
      <linearGradient id="contactA" x1="0" y1="1200" x2="0" y2="1586" gradientUnits="userSpaceOnUse">
        <stop offset="0" stop-color="#ffffff"/><stop offset=".18" stop-color="#d2d6df"/><stop offset=".34" stop-color="#8f95ad"/><stop offset=".5" stop-color="#3b4b84"/><stop offset=".66" stop-color="#0d1a56"/><stop offset="1" stop-color="#0b1550"/>
      </linearGradient>
    </defs>
    <polygon points="0,1200 468,1200 468,1556 234,1586 0,1556" fill="url(#contactA)"/>
  </svg>
  <svg class="band" width="468" height="2107" viewBox="0 0 468 2107" aria-hidden="true">
    <polygon points="0,1921 234,1952 468,1921 468,2107 0,2107" fill="#0b1550"/>
  </svg>

  <!-- header -->
  <a class="nav-link nav-link--active" style="left:43px">HOME</a>
  <a class="nav-link" style="left:93px">ABOUT US</a>
  <div class="brand"><span class="brand-name">CALLOWAY</span><span class="brand-sub">AERONAUTICS</span></div>
  <a class="nav-link" style="left:304px">SERVICES</a>
  <a class="nav-link" style="left:366px">CONTACT US</a>
  <h1 class="hero-title">CALLOWAY<br>AERONAUTICS</h1>
  <div class="pill" style="left:44px;top:176px;width:62px;height:17px;font-size:6.5px">READ MORE</div>

  <span class="divider-dot" style="left:234px;top:264px"></span>

  <!-- services -->
  <h2 class="section-title" style="left:43px;top:319px">OUR<br>SERVICES</h2>
  <p class="lead" style="left:162px;top:311px;width:258px">Calloway buys, sells, leases and facilitates aircraft trading while specializes in structured aircraft investment projects. Calloway has deep industry relationships and years of expertise, allowing to successfully execute lease transactions. We assist airlines, financial institutions and leasing companies when selling or purchasing aircraft.</p>

  <article class="card" style="left:43px;top:402px;height:184px">
    <div class="card-photo" role="img" aria-label="White airliner parked on the apron" style="background:linear-gradient(180deg,#b9cde0 0%,#dfe6ee 55%,#8e959c 100%)"></div>
    <h3 class="card-title">Aircraft Finance</h3>
    <p class="card-text">Lorem ipsum dolor sit amet, consectetur adipiscing elit, sed do eiusmod tempor in cididunt ut laborelor.</p>
  </article>
  <article class="card" style="left:175px;top:402px;height:184px">
    <div class="card-photo" role="img" aria-label="Hands typing on a laptop over an aircraft backdrop" style="background:linear-gradient(160deg,#dbe4ee 0%,#9fb1c6 50%,#eef1f5 100%)"></div>
    <h3 class="card-title">Trading</h3>
    <p class="card-text">Lorem ipsum dolor sit amet, consectetur adipiscing elit, sed do eiusmod tempor in cididunt ut laborelor.</p>
  </article>
  <article class="card" style="left:307px;top:402px;height:184px">
    <div class="card-photo" role="img" aria-label="Airliner climbing after takeoff" style="background:linear-gradient(180deg,#c9d2dc 0%,#e3e8ee 60%,#b8c0ca 100%)"></div>
    <h3 class="card-title">Procurement<br>and Leasing</h3>
    <p class="card-text">Lorem ipsum dolor sit amet, consectetur adipiscing elit, sed do eiusmod tempor.</p>
  </article>

  <span class="divider-dot" style="left:234px;top:640px"></span>

  <!-- about -->
  <div class="about-photo" role="img" aria-label="Wide-body jet lifting off the runway at sunset" style="left:46px;top:707px"></div>
  <h2 class="section-title section-title--light" style="left:238px;top:696px">ABOUT US</h2>
  <div class="about-text" style="left:240px;top:728px">
    <p>Founded in 2011, Calloway Aeronautics’ management has many years of experience in Aviation, a strong background in scheduled airlines with emphasis in all cargo operations, freight forwarding supply chain and freight logistics, as well as ACMI and CMI operations.</p>
    <p>Calloway’s focuses in facilitating wet and dry lease operations, charter and ACMI programs consultancy, aircraft sales, leasing and procurement, aviation consultancy and aircraft management.</p>
  </div>
  <div class="pill" style="left:241px;top:845px;width:76px;height:20px;font-size:7px">READ MORE</div>

  <span class="divider-dot" style="left:234px;top:916px"></span>
  <span class="divider-line" style="top:921px;height:38px"></span>

  <!-- aircraft available -->
  <h2 class="section-title section-title--center" style="top:966px">AIRCRAFT AVAILABLE<br>FOR SALE/LEASE</h2>

  <div class="feat-icon" style="left:43px;top:1047px"><svg width="20" height="20" viewBox="0 0 20 20" fill="none" stroke="#fff" stroke-width="1.2"><path d="M10 1.5l2.2 1.6 2.7-.2.8 2.6 2.2 1.6-.9 2.6.9 2.6-2.2 1.6-.8 2.6-2.7-.2L10 18.5l-2.2-1.6-2.7.2-.8-2.6-2.2-1.6.9-2.6-.9-2.6 2.2-1.6.8-2.6 2.7.2z"/><path d="M7 13l6-6"/><circle cx="7.5" cy="7.5" r="1"/><circle cx="12.5" cy="12.5" r="1"/></svg></div>
  <div class="feat-copy" style="left:90px;top:1050px"><h3 class="feat-title">Sale/Leaseback</h3><p class="feat-text">Sale-leaseback is a method of financing. If your company needs liquidity.</p></div>

  <div class="feat-icon" style="left:43px;top:1103px"><svg width="20" height="20" viewBox="0 0 20 20" fill="none" stroke="#fff" stroke-width="1.2" stroke-linejoin="round"><path d="M3 17l4-1 3-5 5-5c1-1 1-2.5 0-3s-2 0-3 1l-5 5-5 3-1 4z"/><path d="M7 8L3 6l1.5-1.5 6 1M12 13l2 4 1.5-1.5-1-6"/></svg></div>
  <div class="feat-copy" style="left:90px;top:1105px"><h3 class="feat-title">P2F</h3><p class="feat-text">Pandemic has seen the resurgence of operators packing freight.</p></div>

  <div class="feat-icon" style="left:43px;top:1157px"><svg width="20" height="20" viewBox="0 0 20 20" fill="none" stroke="#fff" stroke-width="1.2" stroke-linejoin="round"><path d="M6 3h7l-1 4H8z"/><path d="M8 7v5h4V7"/><path d="M3 18l3-4h5l4-2c1 0 1.5 1 .5 1.5L11 16H6"/></svg></div>
  <div class="feat-copy" style="left:90px;top:1159px;width:96px"><h3 class="feat-title">Wet lease</h3><p class="feat-text">Throughout our deep relationships within the industry, Calloway facilitates short or long-term</p></div>

  <div class="feat-copy" style="left:301px;top:1050px"><h3 class="feat-title">Dry Lease</h3><p class="feat-text">We offer aircraft from our own portfolio on dry lease or could engage</p></div>
  <div class="feat-icon" style="left:387px;top:1047px"><svg width="22" height="22" viewBox="0 0 20 20" fill="none" stroke="#fff" stroke-width="1.1" stroke-linejoin="round"><path d="M2 12l6-2 6-6c1-1 2.5-1 3 0s0 2-1 3l-6 6-2 6-1.5-1 .5-4-3 1-1-1z"/></svg></div>

  <div class="feat-copy" style="left:301px;top:1105px"><h3 class="feat-title">Asset &amp; Aircraft<br>Management</h3><p class="feat-text">We provide aircraft owners Aircraft Management</p></div>
  <div class="feat-icon" style="left:387px;top:1103px"><svg width="22" height="22" viewBox="0 0 20 20" fill="none" stroke="#fff" stroke-width="1.1"><circle cx="10" cy="7" r="3.5"/><circle cx="10" cy="7" r="1.3"/><path d="M3 17c0-2 1.5-3.5 3.5-3.5S10 15 10 17M10 17c0-2 1.5-3.5 3.5-3.5S17 15 17 17"/></svg></div>

  <div class="feat-copy" style="left:301px;top:1159px"><h3 class="feat-title">Worldwide Charters</h3><p class="feat-text">We facilitate the arrangement of full charters to airlines and logistics companies.</p></div>
  <div class="feat-icon" style="left:387px;top:1157px"><svg width="22" height="22" viewBox="0 0 20 20" fill="none" stroke="#fff" stroke-width="1.1"><circle cx="10" cy="10" r="7.5"/><ellipse cx="10" cy="10" rx="3.2" ry="7.5"/><path d="M2.5 10h15M4 6h12M4 14h12"/></svg></div>

  <span class="bracket" style="left:195px;top:1051px;border-top-width:1.2px;border-left-width:1.2px"></span>
  <span class="bracket" style="left:258px;top:1051px;border-top-width:1.2px;border-right-width:1.2px"></span>
  <span class="bracket" style="left:195px;top:1172px;border-bottom-width:1.2px;border-left-width:1.2px"></span>
  <span class="bracket" style="left:258px;top:1172px;border-bottom-width:1.2px;border-right-width:1.2px"></span>
  <div class="ornament" role="img" aria-label="Compass star ornament"></div>

  <div class="pill pill--navy" style="left:179px;top:1216px;width:109px;height:22px;font-size:7.2px">VIEW ALL SERVICES</div>

  <!-- contact -->
  <h2 class="section-title section-title--center section-title--light" style="top:1325px">CONTACT US</h2>
  <p class="contact-sub" style="top:1360px">Sed ut perspiciatis unde omnis iste natus error sit<br>voluptatem accusantium doloremque laud</p>
  <span class="field-label" style="left:100px;top:1403px">Name:</span>
  <span class="field-line" style="left:100px;top:1418px;width:127px"></span>
  <span class="field-label" style="left:241px;top:1403px">Email:</span>
  <span class="field-line" style="left:241px;top:1418px;width:127px"></span>
  <span class="field-label" style="left:100px;top:1430px">Phone:</span>
  <span class="field-line" style="left:100px;top:1445px;width:127px"></span>
  <span class="field-label" style="left:241px;top:1430px">Subject:</span>
  <span class="field-line" style="left:241px;top:1445px;width:127px"></span>
  <span class="field-label" style="left:100px;top:1454px">Message:</span>
  <span class="field-line" style="left:100px;top:1488px;width:265px"></span>
  <div class="pill" style="left:198px;top:1507px;width:73px;height:21px;font-size:7px">SUBMIT</div>

  <span class="divider-dot" style="left:234px;top:1586px"></span>

  <!-- news -->
  <h2 class="section-title section-title--center" style="top:1620px">LATEST NEWS</h2>
  <article class="news-main" style="left:46px;top:1671px">
    <div class="news-main-photo" role="img" aria-label="Jumbo freighter climbing above misty mountains"></div>
    <h3 class="news-main-title">LOREM IPSUM DO<br>LOR SIT LOREAMET,<br>CONSECTETU</h3>
    <p class="news-main-text">Lorem ipsum dolor sit amet,consec tetur adipiscing elit, sed do eiusmod tempor incididunt ut labore</p>
  </article>
  <article class="news-item" style="left:260px;top:1671px">
    <div class="news-thumb" role="img" aria-label="Airliner at the gate under a golden sky" style="background:linear-gradient(180deg,#6f8fb0 0%,#d9b27a 45%,#3d4f62 100%)"></div>
    <p class="news-date">December 18th, 2021</p>
    <h3 class="news-title">LOREM IPSUM DLOR SIT LOREAMETCONSE CTETUR ADIPISCIN.</h3>
    <p class="news-text">Sed ut perspiciatis unde omnis iste natus error sit voluptatem accusantium doloremque laud</p>
  </article>
  <article class="news-item" style="left:260px;top:1787px">
    <div class="news-thumb" role="img" aria-label="Passenger reading in an aircraft cabin" style="background:linear-gradient(160deg,#4a3a3a 0%,#8a5a66 50%,#2f2a30 100%)"></div>
    <p class="news-date">December 18th, 2021</p>
    <h3 class="news-title">LOREM IPSUM DLOR SIT LOREAMETCONSE CTETUR ADIPISCIN.</h3>
    <p class="news-text">Sed ut perspiciatis unde omnis iste natus error sit voluptatem accusantium doloremque laud</p>
  </article>

  <!-- footer -->
  <span class="divider-dot" style="left:234px;top:1960px"></span>
  <div class="foot-brand" style="top:1990px"><span class="brand-name">CALLOWAY</span><span class="brand-sub">AERONAUTICS</span></div>
  <div class="foot-item" style="left:92px;top:2037px"><span class="foot-icon"><svg width="9" height="9" viewBox="0 0 10 10"><path d="M2 1l2 2-1 1.2c.6 1.3 1.5 2.2 2.8 2.8L7 6l2 2-1.2 1.3C4.5 9 1 5.5.7 2.2z" fill="#fff"/></svg></span><span>Phone<br>+1 305 555 0184</span></div>
  <div class="foot-item" style="left:191px;top:2037px"><span class="foot-icon"><svg width="9" height="9" viewBox="0 0 10 10"><rect x="1" y="2.5" width="8" height="5.5" rx=".6" fill="#fff"/><path d="M1.3 3l3.7 2.6L8.7 3" stroke="#8793a6" stroke-width=".8" fill="none"/></svg></span><span>Email<br>info@callowayaero.com</span></div>
  <div class="foot-item" style="left:300px;top:2037px"><span class="foot-icon"><svg width="9" height="9" viewBox="0 0 10 10"><path d="M5 .8a3 3 0 013 3c0 2.2-3 5.6-3 5.6S2 6 2 3.8a3 3 0 013-3z" fill="#fff"/><circle cx="5" cy="3.8" r="1.1" fill="#8793a6"/></svg></span><span>4820 Harbor Ridge Blvd<br>Miramar, FL</span></div>
  <p class="copyright" style="top:2082px">COPYRIGHT © 2021 ALL RIGHT RESERVED</p>
</section>

<!-- ============ Alternate layout ============ -->
<section class="page page--alt">
  <svg class="band" width="468" height="2030" viewBox="0 0 468 2030" role="img" aria-label="Wide-body jet seen head-on against a deep blue sky">
    <defs>
      <linearGradient id="heroSkyB" x1="0" y1="0" x2="0" y2="1">
        <stop offset="0" stop-color="#1a2766"/><stop offset=".6" stop-color="#2f3f86"/><stop offset="1" stop-color="#4e5e9c"/>
      </linearGradient>
    </defs>
    <polygon points="0,0 468,0 468,233 234,264 0,233" fill="url(#heroSkyB)"/>
  </svg>
  <svg class="band" width="468" height="2030" viewBox="0 0 468 2030" role="img" aria-label="Deep blue cloudscape behind the about section">
    <defs>
      <radialGradient id="aboutSkyB" cx=".55" cy=".45" r=".8">
        <stop offset="0" stop-color="#1e3a8c"/><stop offset="1" stop-color="#0a1552"/>
      </radialGradient>
    </defs>
    <polygon points="0,529 234,497 468,529 468,742 234,774 0,742" fill="url(#aboutSkyB)"/>
  </svg>
  <svg class="band" width="468" height="2030" viewBox="0 0 468 2030" role="img" aria-label="Wide-body freighter taking off from a runway, fading into navy">
    <defs>
      <linearGradient id="contactB" x1="0" y1="1110" x2="0" y2="1495" gradientUnits="userSpaceOnUse">
        <stop offset="0" stop-color="#ffffff"/><stop offset=".18" stop-color="#d2d6df"/><stop offset=".34" stop-color="#8f95ad"/><stop offset=".5" stop-color="#3b4b84"/><stop offset=".66" stop-color="#0d1a56"/><stop offset="1" stop-color="#0b1550"/>
      </linearGradient>
    </defs>
    <polygon points="0,1110 468,1110 468,1465 234,1495 0,1465" fill="url(#contactB)"/>
  </svg>
  <svg class="band" width="468" height="2030" viewBox="0 0 468 2030" aria-hidden="true">
    <polygon points="0,1852 234,1882 468,1852 468,2030 0,2030" fill="#0b1550"/>
  </svg>

  <a class="nav-link nav-link--active" style="left:43px">HOME</a>
  <a class="nav-link" style="left:93px">ABOUT US</a>
  <div class="brand"><span class="brand-name">CALLOWAY</span><span class="brand-sub">AERONAUTICS</span></div>
  <a class="nav-link" style="left:304px">SERVICES</a>
  <a class="nav-link" style="left:366px">CONTACT US</a>
  <h1 class="hero-title">CALLOWAY<br>AERONAUTICS</h1>

  <!-- services -->
  <h2 class="section-title section-title--center" style="top:295px">OUR SERVICES</h2>
  <p class="lead" style="left:84px;top:325px;width:300px;text-align:center">Calloway buys, sells, leases and facilitates aircraft trading while specializes in structured aircraft investment projects. Calloway has deep industry relationships and years of expertise, allowing to successfully execute lease transactions. We assist airlines, financial institutions and leasing companies when selling or purchasing aircraft.</p>

  <div class="svc" style="left:53px;top:390px">
    <div class="svc-icon"><svg width="28" height="28" viewBox="0 0 28 28" fill="none" stroke="#fff" stroke-width="1.3"><path d="M6 22V12h5v10M11 22V7h6v15M17 22v-8h5v8M4 22h20"/><path d="M19 5l4 4M23 5l-4 4"/></svg></div>
    <p class="svc-label">Aircraft Finance</p>
  </div>
  <div class="svc" style="left:149px;top:390px">
    <div class="svc-icon"><svg width="28" height="28" viewBox="0 0 28 28" fill="none" stroke="#fff" stroke-width="1.3"><path d="M5 22h18M7 22v-5M11 22v-8M15 22v-6M19 22v-10"/><path d="M6 14l5-5 4 3 7-7M18 5h4v4"/></svg></div>
    <p class="svc-label">Trading</p>
  </div>
  <div class="svc" style="left:239px;top:390px">
    <div class="svc-icon"><svg width="28" height="28" viewBox="0 0 28 28" fill="none" stroke="#fff" stroke-width="1.3"><circle cx="14" cy="9" r="5"/><path d="M14 6v6M12.5 7.5h2.5a1 1 0 010 1.5h-2a1 1 0 000 1.5h2.5"/><path d="M4 19l5-3 5 3 5-3 5 3M9 16v5M19 16v5"/></svg></div>
    <p class="svc-label">Procurement</p>
  </div>
  <div class="svc" style="left:331px;top:390px">
    <div class="svc-icon"><svg width="28" height="28" viewBox="0 0 28 28" fill="none" stroke="#fff" stroke-width="1.3" stroke-linejoin="round"><path d="M9 5h9l-1.5 5h-6z"/><path d="M11 10v6h5v-6"/><path d="M5 24l4-5h6l5-2.5c1.5-.5 2 1 .8 1.8L15 22H9"/></svg></div>
    <p class="svc-label">Leasing</p>
  </div>

  <!-- about -->
  <div class="about-photo" role="img" aria-label="Wide-body jet lifting off the runway at sunset" style="left:47px;top:566px"></div>
  <h2 class="section-title section-title--light" style="left:238px;top:555px">ABOUT US</h2>
  <div class="about-text" style="left:241px;top:587px">
    <p>Founded in 2011, Calloway Aeronautics’ management has many years of experience in Aviation, a strong background in scheduled airlines with emphasis in all cargo operations, freight forwarding supply chain and freight logistics, as well as ACMI and CMI operations.</p>
    <p>Calloway’s focuses in facilitating wet and dry lease operations, charter and ACMI programs consultancy, aircraft sales, leasing and procurement, aviation consultancy and aircraft management.</p>
  </div>
  <div class="pill" style="left:241px;top:703px;width:76px;height:20px;font-size:7px">READ MORE</div>

  <span class="divider-dot" style="left:234px;top:774px"></span>
  <span class="divider-line" style="top:779px;height:40px"></span>

  <h2 class="section-title section-title--center" style="top:827px">AIRCRAFT AVAILABLE<br>FOR SALE/LEASE</h2>

  <article class="card" style="left:44px;top:892px;height:216px">
    <div class="card-photo" role="img" aria-label="White airliner parked on the apron" style="background:linear-gradient(180deg,#b9cde0 0%,#dfe6ee 55%,#8e959c 100%)"></div>
    <h3 class="card-title" style="margin-top:20px">Sale/Leaseback</h3>
    <p class="card-text">Sale-leaseback is a method of financing. If your company needs liquidity, your aircraft or engine can serve as collateral for a loan throughout a sale leaseback transaction.</p>
    <span class="card-btn">READ MORE</span>
  </article>
  <article class="card" style="left:176px;top:892px;height:216px">
    <div class="card-photo" role="img" aria-label="Passenger working on a laptop in an aircraft seat" style="background:linear-gradient(160deg,#c9d3dd 0%,#7e8fa2 50%,#2c3540 100%)"></div>
    <h3 class="card-title" style="margin-top:14px">Passenger to Freighter<br>Conversion (P2F)</h3>
    <p class="card-text">Pandemic has seen the resurgence of operators packing freight into the main cabins of passenger aircraft. Carriers have been allowed to transport</p>
    <span class="card-btn">READ MORE</span>
  </article>
  <article class="card" style="left:308px;top:892px;height:216px">
    <div class="card-photo" role="img" aria-label="Airliner climbing after takeoff" style="background:linear-gradient(180deg,#c9d2dc 0%,#e3e8ee 60%,#b8c0ca 100%)"></div>
    <h3 class="card-title" style="margin-top:20px">Wet lease</h3>
    <p class="card-text">Throughout our deep relationships within the industry, Calloway facilitates short or long-term wet leases to airlines and qualified parties around the globe, whereby we provide.</p>
    <span class="card-btn">READ MORE</span>
  </article>

  <div class="pill pill--navy" style="left:179px;top:1151px;width:111px;height:22px;font-size:7.2px">VIEW ALL SERVICES</div>

  <!-- contact -->
  <h2 class="section-title section-title--center section-title--light" style="top:1246px">CONTACT US</h2>
  <p class="contact-sub" style="top:1281px">Sed ut perspiciatis unde omnis iste natus error sit<br>voluptatem accusantium doloremque laud</p>
  <span class="field-label" style="left:101px;top:1323px">Name:</span>
  <span class="field-line" style="left:101px;top:1338px;width:127px"></span>
  <span class="field-label" style="left:241px;top:1323px">Email:</span>
  <span class="field-line" style="left:241px;top:1338px;width:127px"></span>
  <span class="field-label" style="left:101px;top:1350px">Phone:</span>
  <span class="field-line" style="left:101px;top:1365px;width:127px"></span>
  <span class="field-label" style="left:241px;top:1350px">Subject:</span>
  <span class="field-line" style="left:241px;top:1365px;width:127px"></span>
  <span class="field-label" style="left:101px;top:1374px">Message:</span>
  <span class="field-line" style="left:101px;top:1409px;width:265px"></span>
  <div class="pill" style="left:198px;top:1428px;width:74px;height:21px;font-size:7px">SUBMIT</div>

  <span class="divider-dot" style="left:234px;top:1495px"></span>

  <h2 class="section-title section-title--center" style="top:1533px">LATEST NEWS</h2>
  <article class="news-main" style="left:47px;top:1582px">
    <div class="news-main-photo" role="img" aria-label="Jumbo freighter climbing above misty mountains"></div>
    <h3 class="news-main-title" style="left:35px">LOREM IPSUM DO<br>LOR SIT LOREAMET,<br>CONSECTETU</h3>
    <p class="news-main-text" style="left:35px">Lorem ipsum dolor sit amet,consec tetur adipiscing elit, sed do eiusmod tempor incididunt ut labore</p>
  </article>
  <article class="news-item" style="left:261px;top:1582px">
    <div class="news-thumb" role="img" aria-label="Airliner at the gate under a golden sky" style="background:linear-gradient(180deg,#6f8fb0 0%,#d9b27a 45%,#3d4f62 100%)"></div>
    <p class="news-date">December 18th, 2021</p>
    <h3 class="news-title">LOREM IPSUM DLOR SIT LOREAMETCONSE CTETUR ADIPISCIN.</h3>
    <p class="news-text">Sed ut perspiciatis unde omnis iste natus error sit voluptatem accusantium doloremque laud</p>
  </article>
  <article class="news-item" style="left:261px;top:1698px">
    <div class="news-thumb" role="img" aria-label="Passenger reading in an aircraft cabin" style="background:linear-gradient(160deg,#4a3a3a 0%,#8a5a66 50%,#2f2a30 100%)"></div>
    <p class="news-date">December 18th, 2021</p>
    <h3 class="news-title">LOREM IPSUM DLOR SIT LOREAMETCONSE CTETUR ADIPISCIN.</h3>
    <p class="news-text">Sed ut perspiciatis unde omnis iste natus error sit voluptatem accusantium doloremque laud</p>
  </article>

  <span class="divider-dot" style="left:234px;top:1886px"></span>
  <div class="foot-brand" style="top:1910px"><span class="brand-name">CALLOWAY</span><span class="brand-sub">AERONAUTICS</span></div>
  <div class="foot-item" style="left:93px;top:1961px"><span class="foot-icon"><svg width="9" height="9" viewBox="0 0 10 10"><path d="M2 1l2 2-1 1.2c.6 1.3 1.5 2.2 2.8 2.8L7 6l2 2-1.2 1.3C4.5 9 1 5.5.7 2.2z" fill="#fff"/></svg></span><span>Phone<br>+1 305 555 0184</span></div>
  <div class="foot-item" style="left:192px;top:1961px"><span class="foot-icon"><svg width="9" height="9" viewBox="0 0 10 10"><rect x="1" y="2.5" width="8" height="5.5" rx=".6" fill="#fff"/><path d="M1.3 3l3.7 2.6L8.7 3" stroke="#8793a6" stroke-width=".8" fill="none"/></svg></span><span>Email<br>info@callowayaero.com</span></div>
  <div class="foot-item" style="left:301px;top:1961px"><span class="foot-icon"><svg width="9" height="9" viewBox="0 0 10 10"><path d="M5 .8a3 3 0 013 3c0 2.2-3 5.6-3 5.6S2 6 2 3.8a3 3 0 013-3z" fill="#fff"/><circle cx="5" cy="3.8" r="1.1" fill="#8793a6"/></svg></span><span>4820 Harbor Ridge Blvd<br>Miramar, FL</span></div>
  <p class="copyright" style="top:2005px">COPYRIGHT © 2021 ALL RIGHT RESERVED</p>
</section>

</main>
</body>
</html>
```